Business Card Design

We need a business card design for our new expansion based in Bloomfield Hills, Michigan. Our company is Quiet Harbor Institute & Wellness Center. Our Academy teaches individuals of all ages and professions to live from their soul. We teach intuitive development, meditation and mindfulness; shamanic healing. And ourr healing center provides holistic services. We offer certification programs that support the ethical practices of Intuitive professionals. Our team of Intuitive Practitioners includes: doctors, psychologists, chiropractor, soul retrievers, mediums, etc who all balance their knowledge with intuitive wisdom.

We want our symbol to be the Blue Morpho Buttefly and the colors on the card to complement it. We want to communicate inspiration, healing and empowerment. Thank you
Updates

Industry/Entity Type

Business

Contact Information for Business Card

Dana Orwick
Medium. Author. Soul Retriever.
Founder, Quiet Harbor

Quiet Harbor

19 North Cedar Mill Drive Suite 100
Fernwood Heights, MI 48517
248-603-7418

www.danaorwick.example

Requirements
Must have
• blue morpho butterfly

```html
<!DOCTYPE html>
<html lang="en">
<head>
<meta charset="utf-8">
<title>Dana Orwick — Business Card</title>
<link href="https://fonts.googleapis.com/css2?family=Questrial&display=swap" rel="stylesheet">
<style>
  :root {
    --backdrop: #e9ebee;
    --card-white: #ffffff;
    --card-shade: #f1f2f4;
    --cyan: #1fb6e4;
    --cyan-deep: #0fa6d8;
    --cyan-light: #17d4ee;
    --ink-grey: #8a8d91;
    --ink-soft: #a9acb0;
    --ink-dark: #6f7276;
  }
  * { box-sizing: border-box; margin: 0; padding: 0; }
  html, body {
    width: 1200px; height: 901px; overflow: hidden;
    background: var(--backdrop);
    font-family: "Questrial", sans-serif;
  }
  .stage {
    position: relative; width: 1200px; height: 901px;
  }
  .card {
    position: absolute; left: 300px; width: 600px; height: 343px;
    border-radius: 3px;
    box-shadow: 0 6px 18px rgba(0,0,0,.12);
    overflow: hidden;
  }
  /* Back side */
  .card--back {
    top: 72px;
    background: linear-gradient(135deg, var(--cyan-light), var(--cyan-deep));
    color: var(--card-white);
  }
  .card--back .brand {
    position: absolute; left: 0; right: 0; top: 120px;
    display: flex; align-items: center; justify-content: center; gap: 16px;
  }
  .brand__dot {
    width: 34px; height: 34px; border-radius: 50%;
    background: currentColor; opacity: .9;
  }
  .card--back .brand__name { font-size: 44px; letter-spacing: .5px; }
  .card--back .brand__tagline {
    position: absolute; left: 0; right: 0; top: 186px;
    text-align: center; font-size: 18px;
  }
  .card--back .website {
    position: absolute; left: 0; right: 0; bottom: 40px;
    text-align: center; font-size: 13px; letter-spacing: 5px;
    color: rgba(255,255,255,.85);
  }
  /* Front side */
  .card--front {
    top: 486px;
    background: linear-gradient(160deg, var(--card-white) 40%, var(--card-shade));
  }
  .card--front .brand {
    position: absolute; left: 40px; top: 44px;
    display: flex; align-items: center; gap: 10px; color: var(--cyan);
  }
  .card--front .brand__dot { width: 22px; height: 22px; }
  .card--front .brand__name { font-size: 24px; color: var(--ink-dark); }
  .card--front .brand__tagline {
    position: absolute; left: 72px; top: 80px;
    font-size: 12px; color: var(--cyan);
  }
  .person {
    position: absolute; right: 40px; top: 42px; text-align: right;
  }
  .person__name { font-size: 22px; color: var(--cyan); letter-spacing: 1px; }
  .person__cred { color: var(--ink-dark); }
  .person__role {
    font-size: 12.5px; color: var(--ink-soft); line-height: 1.3; letter-spacing: .6px;
  }
  .contact {
    position: absolute; left: 40px; bottom: 50px;
    list-style: none; font-size: 15px; color: var(--ink-grey); letter-spacing: 1px;
  }
  .contact__item { display: flex; align-items: flex-start; gap: 14px; margin-top: 16px; line-height: 1.2; }
  .contact__icon { flex: none; width: 20px; height: 20px; margin-top: 0; }
</style>
</head>
<body>
<main class="stage">

  <section class="card card--back" aria-label="Card back">
    <div class="brand">
      <span class="brand__dot" aria-hidden="true"></span>
      <span class="brand__name">Dana Orwick</span>
    </div>
    <p class="brand__tagline">Quiet Harbor</p>
    <p class="website">www.danaorwick.example</p>
  </section>

  <section class="card card--front" aria-label="Card front">
    <div class="brand">
      <span class="brand__dot" aria-hidden="true"></span>
      <span class="brand__name">Dana Orwick</span>
    </div>
    <p class="brand__tagline">Quiet Harbor</p>

    <div class="person">
      <p class="person__name">Dana Orwick, <span class="person__cred">M.A.</span></p>
      <p class="person__role">Medium. Author. Soul Retriever<br>Founder, Quiet Harbor</p>
    </div>

    <ul class="contact">
      <li class="contact__item">
        <svg class="contact__icon" viewBox="0 0 20 20" aria-hidden="true">
          <circle cx="10" cy="10" r="9" fill="none" stroke="var(--cyan)" stroke-width="1.6"/>
          <path d="M7 5.5c-1 .6-1.4 1.6-.9 3 .8 2.3 2.6 4.3 4.9 5.3 1.2.5 2.2.2 2.9-.8l-1.8-1.5-1.2.7c-1.2-.6-2.1-1.6-2.6-2.8l.8-1.1z" fill="var(--cyan)"/>
        </svg>
        <span>248-603-7418</span>
      </li>
      <li class="contact__item">
        <svg class="contact__icon" viewBox="0 0 20 20" aria-hidden="true">
          <circle cx="10" cy="10" r="9" fill="none" stroke="var(--cyan)" stroke-width="1.6"/>
          <path d="M10 4.5a3.3 3.3 0 0 0-3.3 3.3c0 2.5 3.3 6.5 3.3 6.5s3.3-4 3.3-6.5A3.3 3.3 0 0 0 10 4.5z" fill="var(--cyan)"/>
          <circle cx="10" cy="7.8" r="1.2" fill="var(--card-white)"/>
        </svg>
        <span>19 North Cedar Mill Drive, Suite 100<br>Fernwood Heights, MI 48517</span>
      </li>
    </ul>
  </section>

</main>
</body>
</html>
```